KL MOTORS BANNER/SIGN DESIGN

Design a banner sign for outdoor use for KL MOTORS - a premium pre owned vehicle sales center. The size must be 36 feet in width
and 3 feet in height.

Information required: logo (attached)
-PREMIUM PRE-OWEND VEHICLE SALES
- 517.264.3081

perhaps in smaller font: BUY-SELL-TRADE

prefer white background but could possibly do red matching the logo

```html
<!DOCTYPE html>
<html lang="en">
<head>
<meta charset="utf-8">
<title>KL Motors Banner</title>
<link rel="stylesheet" href="https://fonts.googleapis.com/css2?family=Barlow+Semi+Condensed:wght@700&family=Roboto:wght@700;900&display=swap">
<style>
  :root {
    --canvas-grey: #b3b3b3;
    --banner-white: #ffffff;
    --brand-red: #dc0000;
    --ink-black: #111111;
    --text-white: #ffffff;
  }
  html, body {
    margin: 0;
    padding: 0;
    width: 1200px;
    height: 1200px;
    overflow: hidden;
    background: var(--canvas-grey);
  }
  .stage {
    position: relative;
    width: 1200px;
    height: 1200px;
  }
  .banner {
    position: absolute;
    left: 0;
    top: 0;
  }
  .brand-name {
    font-family: "Roboto", Arial, sans-serif;
    font-weight: 900;
    fill: var(--ink-black);
  }
  .tagline-small {
    font-family: "Barlow Semi Condensed", "Arial Narrow", sans-serif;
    font-weight: 700;
    fill: var(--text-white);
  }
  .headline {
    font-family: "Barlow Semi Condensed", "Arial Narrow", sans-serif;
    font-weight: 700;
    fill: var(--text-white);
  }
  .phone-line {
    font-family: "Roboto", Arial, sans-serif;
    font-weight: 700;
    fill: var(--text-white);
  }
</style>
</head>
<body>
  <main class="stage">
    <svg class="banner" width="1200" height="1200" viewBox="0 0 1200 1200" xmlns="http://www.w3.org/2000/svg">
      <!-- white logo panel -->
      <rect class="logo-panel" x="66" y="555" width="300" height="89" fill="var(--banner-white)"/>
      <!-- red message band with arrow notch -->
      <polygon class="message-band" points="348,555 1134,555 1134,644 348,644 397,599.5" fill="var(--brand-red)"/>

      <!-- brand name with a plain circle -->
      <circle class="brand-dot" cx="112" cy="599.5" r="28" fill="none" stroke="var(--brand-red)" stroke-width="5"/>
      <text class="brand-name" x="152" y="613" font-size="36" textLength="196" lengthAdjust="spacingAndGlyphs">KL MOTORS</text>

      <!-- message -->
      <text class="tagline-small" x="764" y="578" font-size="19" text-anchor="middle" textLength="158" lengthAdjust="spacingAndGlyphs">BUY-SELL-TRADE</text>
      <text class="headline" x="763" y="616" font-size="45" text-anchor="middle" textLength="683" lengthAdjust="spacingAndGlyphs">PREMIUM PRE-OWEND VEHICLE SALES</text>
      <text class="phone-line" x="764" y="636" font-size="20" text-anchor="middle" textLength="234" lengthAdjust="spacingAndGlyphs">CALL: 517.264.3081</text>
    </svg>
  </main>
</body>
</html>
```